Design Challege - Simplify a Complex Message

We have a new website design, but one of the pages presents a particular problem.

Our company does ERP implementations. We have developed a proprietary approach to these implementations based on the idea that you must get eight (and only eight) things right. These eight things are listed below, summarized in one or two words each:

1. Value
2. Capability
3. Functionality
4. Data
5. Technology
6. Change Leadership
7. Quality
8. Governance

Each of these eight things can be summarized in a short paragraph, but when you combine all eight summaries with a brief introductory text, the result is a lot of text - so much text that the casual surfer may be overwhelmed by it.

The winning design will find an engaging way to present the information in a way that presents a high-level summary, using icons and one- or two-word descriptions above but revealing more information when clicked.

Our current design for this information, with a paragraph describing the eight elements in a table, is included as an upload in PDF and Microsoft Word formats. We are looking for a creative way to display these eight things, showing the detail only when the user wants to see it.

The website is being built in WordPress, using Elementor as a page builder.

We will implement (code) the page, but the winner will be asked to specify the widget or other add-in if one is required.

The design does not need to include a header or footer, we have those.

Target Market(s)

Business executives working in technology

Industry/Entity Type

Any

Number of Pages Required

1 page

Font styles to use
Sans Serif

Requirements
Must have
• A design for the body of the page, but not the header or footer.
Nice to have
• Unique icons or images appropriate for each of the eight things.
Should not have
• A lot of text on one page

```html
<!DOCTYPE html>
<html lang="en">
<head>
<meta charset="utf-8">
<title>Eight Things to Get Right</title>
<link rel="stylesheet" href="https://fonts.googleapis.com/css2?family=Poppins:wght@400;500;600;700&display=swap">
<style>
  :root {
    --ink: #111111;
    --body: #3d3d3d;
    --brand: #0a4a94;
    --navy: #03346a;
    --link: #0b3c78;
    --link-active: #1ea0dc;
    --sky-1: #0aa9e0;
    --sky-2: #0a7fc2;
    --card: #ffffff;
    --page: #ffffff;
  }
  * { box-sizing: border-box; margin: 0; padding: 0; }
  html, body { width: 1200px; height: 985px; overflow: hidden; background: var(--page); }
  body { font-family: "Poppins", sans-serif; color: var(--ink); position: relative; }

  .intro { position: absolute; top: 100px; left: 0; width: 1200px; text-align: center; }
  .intro__title { font-size: 34px; font-weight: 600; line-height: 48px; letter-spacing: -0.2px; }
  .intro__title span { color: var(--brand); }
  .intro__text { font-size: 13px; line-height: 20.5px; color: var(--ink); margin-top: 17px; }
  .intro__text + .intro__text { margin-top: 13px; }

  .pillars {
    position: absolute; top: 348px; left: 141px;
    display: grid; grid-template-columns: repeat(4, 212px);
    column-gap: 23.5px; row-gap: 67px;
  }
  .pillar {
    position: relative; height: 222px; background: var(--card);
    border-radius: 8px; box-shadow: 0 2px 12px rgba(20, 40, 80, 0.09);
    text-align: center; padding: 51px 10px 0;
  }
  .pillar__icon {
    position: absolute; top: -35px; left: 71px; width: 70px; height: 70px;
    border-radius: 50%; background: linear-gradient(135deg, var(--sky-1), var(--sky-2));
    box-shadow: 0 0 0 6px var(--card);
  }
  .pillar__name { font-size: 13.5px; font-weight: 600; letter-spacing: 0.4px; line-height: 18px; }
  .pillar__summary { font-size: 12.5px; line-height: 19px; color: var(--body); margin-top: 7px; height: 95px; }
  .pillar__link {
    display: inline-flex; align-items: center; gap: 4px; margin-top: 10px;
    font-size: 12.5px; font-weight: 500; color: var(--link); text-decoration: none;
  }
  .pillar__link svg { width: 15px; height: 10px; }

  .pillar--active { background: var(--navy); box-shadow: 0 6px 18px rgba(3, 52, 106, 0.25); }
  .pillar--active .pillar__name,
  .pillar--active .pillar__summary { color: #ffffff; }
  .pillar--active .pillar__link { color: var(--link-active); }
  .pillar--active .pillar__icon { box-shadow: 0 0 0 6px #ffffff; }
</style>
</head>
<body>
  <header class="intro">
    <h1 class="intro__title">Eight Things to <span>Get Right</span></h1>
    <p class="intro__text">Like the roots and branches of a tree, there are many considerations in an ERP implementation.<br>Focus too much on the minor details, and you can lose sight of the tree.</p>
    <p class="intro__text">In an ERP implementation, you must get eight major things right to be successful.<br>Ignore any of them, and your implementation will fail. Get them right, and you will likely succeed.</p>
  </header>

  <main class="pillars">
    <article class="pillar pillar--active">
      <div class="pillar__icon" role="img" aria-label="Icon of coins and a rising arrow"></div>
      <h2 class="pillar__name">VALUE</h2>
      <p class="pillar__summary">The project must provide value that significantly exceeds potential project costs and should be aligned with the company’s...</p>
      <a class="pillar__link" href="#">Learn More <svg viewBox="0 0 15 10"><path d="M0 5h13M9 1l4 4-4 4" fill="none" stroke="currentColor" stroke-width="1.5"/></svg></a>
    </article>
    <article class="pillar">
      <div class="pillar__icon" role="img" aria-label="Icon of a growth chart, gear and person"></div>
      <h2 class="pillar__name">CAPABILITY</h2>
      <p class="pillar__summary">The company and the implementation team must be capable of implementing the project on their own or with help. The project must...</p>
      <a class="pillar__link" href="#">Learn More <svg viewBox="0 0 15 10"><path d="M0 5h13M9 1l4 4-4 4" fill="none" stroke="currentColor" stroke-width="1.5"/></svg></a>
    </article>
    <article class="pillar">
      <div class="pillar__icon" role="img" aria-label="Icon of a gear with a wrench"></div>
      <h2 class="pillar__name">FUNCTIONALITY</h2>
      <p class="pillar__summary">An ERP project must support required business processes, both now and in the future. A systematic review of all business processes...</p>
      <a class="pillar__link" href="#">Learn More <svg viewBox="0 0 15 10"><path d="M0 5h13M9 1l4 4-4 4" fill="none" stroke="currentColor" stroke-width="1.5"/></svg></a>
    </article>
    <article class="pillar">
      <div class="pillar__icon" role="img" aria-label="Icon of a data dashboard with charts"></div>
      <h2 class="pillar__name">DATA</h2>
      <p class="pillar__summary">ERP systems are data-hungry creatures. Please be careful before assuming that because so much data goes into them, an equal...</p>
      <a class="pillar__link" href="#">Learn More <svg viewBox="0 0 15 10"><path d="M0 5h13M9 1l4 4-4 4" fill="none" stroke="currentColor" stroke-width="1.5"/></svg></a>
    </article>
    <article class="pillar">
      <div class="pillar__icon" role="img" aria-label="Icon of a globe inside a gear with circuit lines"></div>
      <h2 class="pillar__name">TECHNOLOGY</h2>
      <p class="pillar__summary">What is the platform for the system? Is it offered by a vendor that will be around for as long as your system? Will it integrate with...</p>
      <a class="pillar__link" href="#">Learn More <svg viewBox="0 0 15 10"><path d="M0 5h13M9 1l4 4-4 4" fill="none" stroke="currentColor" stroke-width="1.5"/></svg></a>
    </article>
    <article class="pillar">
      <div class="pillar__icon" role="img" aria-label="Icon of a leader with a team"></div>
      <h2 class="pillar__name">CHANGE LEADERSHIP</h2>
      <p class="pillar__summary">Change leadership (often called change management) considers the human side of an ERP implementation. Change is hard, even if...</p>
      <a class="pillar__link" href="#">Learn More <svg viewBox="0 0 15 10"><path d="M0 5h13M9 1l4 4-4 4" fill="none" stroke="currentColor" stroke-width="1.5"/></svg></a>
    </article>
    <article class="pillar">
      <div class="pillar__icon" role="img" aria-label="Icon of a quality award badge with thumbs up"></div>
      <h2 class="pillar__name">QUALITY</h2>
      <p class="pillar__summary">Quality is multi-dimensional, and it’s more than a measurement; it’s a perception. An ERP needs to be reliable...</p>
      <a class="pillar__link" href="#">Learn More <svg viewBox="0 0 15 10"><path d="M0 5h13M9 1l4 4-4 4" fill="none" stroke="currentColor" stroke-width="1.5"/></svg></a>
    </article>
    <article class="pillar">
      <div class="pillar__icon" role="img" aria-label="Icon of a handshake with a group"></div>
      <h2 class="pillar__name">GOVERNANCE</h2>
      <p class="pillar__summary">ERP projects require both management and leadership. Planning, changing plans, communication, decision making, and...</p>
      <a class="pillar__link" href="#">Learn More <svg viewBox="0 0 15 10"><path d="M0 5h13M9 1l4 4-4 4" fill="none" stroke="currentColor" stroke-width="1.5"/></svg></a>
    </article>
  </main>
</body>
</html>
```